Corvane Transit Assoc needs Info graphic 1 pager (front & back)

We are looking for design work for an infographic type 1 pager (front and back). We will provide the information for the project. I need your help in the layout. Please see attachments for a general idea and direction. I value your design ideas, though, so please feel free to add your personal touch.

Front page is the new infographic that you are creating based off of my hand drafted sketch.

Back page is simply using the Flowchart from the Tellis Review Bureau.

Target Market(s)

State Legislators

Industry/Entity Type

Work

Requirements
Must have
• Nice looking info graphic one-pager. Please try to use the photos I sent in the graphic or similar rail clip art. Make the numbers stand out where possible. Give them emphasis.
• Make it clean. I want to share this info in short/quick meetings with legislators. I want it easy to decipher.
Nice to have
• Bold, strong colors.

```html
<!DOCTYPE html>
<html lang="en">
<head>
<meta charset="utf-8">
<title>Public Act 51 – Freight Railroad Funding</title>
<link rel="stylesheet" href="https://fonts.googleapis.com/css2?family=Oswald:wght@500;600;700&family=Arimo:wght@400;700&family=Libre+Baskerville:wght@700&display=swap">
<style>
  :root {
    --navy: #0b0f6b;
    --maroon: #5a0a0a;
    --maroon-deep: #440505;
    --red: #e4131b;
    --yellow: #fcc800;
    --gold: #f2c21b;
    --sky: #3a8ede;
    --white: #ffffff;
    --ink: #1c1c1c;
    --page: #f4f4f4;
  }
  * { margin: 0; padding: 0; box-sizing: border-box; }
  html, body { width: 902px; height: 1200px; overflow: hidden; background: var(--page); }
  .sheet { position: relative; width: 902px; height: 1200px; background: var(--white); font-family: "Arimo", Arial, sans-serif; color: var(--ink); overflow: hidden; }

  .masthead { position: absolute; left: 0; top: 0; width: 902px; height: 188px; background: var(--navy); text-align: center; color: var(--white); }
  .masthead h1 { font-family: "Oswald", sans-serif; font-weight: 600; font-size: 84px; line-height: 1; padding-top: 18px; letter-spacing: 0.5px; }
  .masthead h2 { font-family: "Arimo", sans-serif; font-weight: 700; font-size: 54px; line-height: 1; margin-top: 10px; }
  .rule { position: absolute; left: 0; top: 188px; width: 902px; height: 12px; background: var(--yellow); }

  .funding { position: absolute; left: 0; top: 200px; width: 902px; height: 527px; background: var(--maroon); }
  .fund-chart { position: absolute; left: 0; top: 0; width: 462px; height: 527px; }
  .fund-chart .caption { position: absolute; left: 37px; top: 22px; font-size: 19px; font-weight: 700; line-height: 1.3; }
  .fund-chart .uses { position: absolute; left: 113px; top: 458px; font-size: 16px; font-weight: 700; line-height: 1.4; }

  .stat { position: absolute; border: 3px solid var(--white); border-radius: 8px; display: flex; align-items: center; }
  .stat .big { font-family: "Oswald", sans-serif; font-weight: 700; line-height: 1; }
  .stat .label { font-weight: 700; text-transform: uppercase; line-height: 1.15; white-space: nowrap; }
  .stat-budget { left: 503px; top: 14px; width: 359px; height: 112px; background: var(--red); padding-left: 10px; }
  .stat-budget .big { font-size: 84px; color: var(--white); }
  .stat-budget .label { margin-left: 12px; color: var(--ink); }
  .stat-budget .label strong { display: block; font-family: "Oswald", sans-serif; font-size: 42px; line-height: 1; }
  .stat-budget .label span { font-size: 18px; }
  .stat-share { left: 503px; top: 146px; width: 359px; height: 94px; background: var(--yellow); padding-left: 8px; }
  .stat-share .big { font-size: 56px; color: var(--white); }
  .stat-share .label { margin-left: 12px; font-size: 17px; color: var(--ink); }
  .stat-autos { left: 503px; top: 259px; width: 359px; height: 109px; background: var(--red); padding-left: 8px; }
  .stat-autos .big { font-size: 78px; color: var(--white); }
  .stat-autos .label { margin-left: 12px; font-size: 17px; color: var(--ink); }
  .stat-small { top: 390px; height: 127px; background: var(--maroon-deep); border-radius: 6px; flex-direction: column; justify-content: center; text-align: center; color: var(--white); }
  .stat-small .big { color: var(--gold); font-size: 48px; }
  .stat-small .label { font-size: 16px; }
  .stat-roads { left: 508px; width: 164px; }
  .stat-miles { left: 690px; width: 165px; }
  .stat-miles .label { font-size: 20px; margin-bottom: 6px; }

  .safety-band { position: absolute; left: 0; top: 737px; width: 902px; height: 176px; }
  .track-photo { position: absolute; inset: 0; background: linear-gradient(90deg, #f1f1ef 0%, #e3e2dc 40%, #bfbab0 65%, #d8d6cf 100%); }
  .sign-photo { position: absolute; left: 60px; top: 9px; width: 98px; height: 168px; background: linear-gradient(180deg, #8aa5c4 0%, #6b7d6a 60%, #3a3a34 100%); }
  .safety-band h3 { position: absolute; left: 232px; top: 48px; font-family: "Arimo", sans-serif; font-weight: 700; font-size: 72px; color: var(--red); line-height: 1; }
  .xing-placeholder { position: absolute; left: 598px; top: 6px; width: 164px; height: 164px; border-radius: 50%; background: radial-gradient(circle at 40% 35%, #f6e35a 0%, #e8b800 70%, #9a9a9a 100%); }

  .program { position: absolute; top: 913px; height: 154px; }
  .program-left { left: 0; width: 448px; }
  .program-right { left: 454px; width: 448px; }
  .program h4 { height: 52px; background: var(--navy); color: var(--white); font-size: 24px; font-weight: 700; display: flex; align-items: center; justify-content: center; }
  .program .body { height: 102px; background: var(--sky); display: flex; align-items: center; padding-left: 34px; }
  .program .amount { font-family: "Oswald", sans-serif; font-weight: 700; font-size: 56px; color: var(--red); -webkit-text-stroke: 2px var(--white); paint-order: stroke fill; line-height: 1; }
  .program p { margin-left: 22px; font-size: 15px; font-weight: 700; color: var(--white); line-height: 1.25; }

  .footer { position: absolute; left: 0; top: 1067px; width: 902px; height: 133px; background: var(--white); }
  .footer-wedge { position: absolute; right: 0; bottom: 0; }
  .assoc-name { position: absolute; left: 34px; top: 38px; width: 170px; font-family: "Libre Baskerville", serif; font-weight: 700; font-size: 20px; line-height: 1.2; color: var(--navy); text-align: center; }
  .total-share { position: absolute; left: 223px; top: 22px; width: 617px; height: 90px; background: var(--navy); border: 3px solid var(--white); box-shadow: 0 0 0 2px var(--navy); border-radius: 6px; display: flex; align-items: center; color: var(--white); font-size: 21px; font-weight: 700; padding-left: 20px; }
  .total-share .big { font-family: "Oswald", sans-serif; font-size: 80px; color: var(--yellow); margin: 0 16px; line-height: 1; }
  .total-share .tail { line-height: 1.2; }
</style>
</head>
<body>
<main class="sheet">
  <header class="masthead">
    <h1>PUBLIC ACT 51 OF 195</h1>
    <h2>Freight Railroad&nbsp; funding</h2>
  </header>
  <div class="rule"></div>

  <section class="funding">
    <div class="fund-chart">
      <svg width="462" height="527" viewBox="0 0 462 527" aria-hidden="true" style="position:absolute;left:0;top:0">
        <defs>
          <radialGradient id="pieFill" cx="50%" cy="45%" r="60%">
            <stop offset="0" stop-color="#b81c1c"/>
            <stop offset="1" stop-color="#6a0808"/>
          </radialGradient>
        </defs>
        <polygon points="0,0 462,0 462,527 0,527" fill="#ffffff"/>
        <polygon points="0,380 60,527 0,527" fill="#5a0a0a"/>
        <circle cx="236" cy="255" r="184" fill="#ffffff" stroke="#dcdcdc" stroke-width="2"/>
        <circle cx="236" cy="255" r="176" fill="url(#pieFill)"/>
        <path d="M236 255 L192 425 A176 176 0 0 0 216 430 Z" fill="#ffffff"/>
        <circle cx="236" cy="255" r="11" fill="#ffffff"/>
        <text x="193" y="212" fill="#ffffff" font-family="Arimo, sans-serif" font-weight="700" font-size="22">CTF</text>
        <text x="193" y="241" fill="#ffffff" font-family="Arimo, sans-serif" font-weight="700" font-size="22">$320 Sm</text>
        <text x="99" y="371" fill="#ffffff" font-family="Arimo, sans-serif" font-weight="700" font-size="15">Freight Rail</text>
        <text x="240" y="385" fill="#ffffff" font-family="Arimo, sans-serif" font-size="66">2%</text>
      </svg>
      <p class="caption">Comprehensive Trasporation Fund<br>Upto 10% of MTF= Sec. 10(1)(n)</p>
      <p class="uses">Freight Economic Development<br>Freight Property management</p>
    </div>

    <div class="stat stat-budget"><span class="big">$ 4.1</span><span class="label"><strong>BILLION</strong><span>CTD BUDGET</span></span></div>
    <div class="stat stat-share"><span class="big">20%</span><span class="label">Portion of freight<br>moved BT rail in MT</span></div>
    <div class="stat stat-autos"><span class="big">75%</span><span class="label">of all finished<br>automobiles<br>leave MI on rail</span></div>
    <div class="stat stat-small stat-roads"><span class="big">28</span><span class="label">Freigt<br>railroads<br>in MI</span></div>
    <div class="stat stat-small stat-miles"><span class="label">Miles of<br>travel</span><span class="big">3,600</span></div>
  </section>

  <section class="safety-band">
    <div class="track-photo" role="img" aria-label="Photo of railroad tracks on gravel ballast"></div>
    <div class="sign-photo" role="img" aria-label="Photo of a railroad crossing sign with signal lights"></div>
    <h3>SAFETY</h3>
    <div class="xing-placeholder" role="img" aria-label="Round yellow railroad crossing warning sign illustration"></div>
  </section>

  <section class="program program-left">
    <h4>Crossing Safety Program:</h4>
    <div class="body"><span class="amount">$3m</span><p>Provides Funds for the elimination<br>of hazards at railway-highway<br>crossings</p></div>
  </section>
  <section class="program program-right">
    <h4>Local surface Grade Crossing:</h4>
    <div class="body"><span class="amount">$3m</span><p>Help locals railroads partner to<br>better maintain local crossing<br>surfaces for the motoring public</p></div>
  </section>

  <footer class="footer">
    <svg class="footer-wedge" width="320" height="133" viewBox="0 0 320 133" aria-hidden="true">
      <polygon points="320,0 320,133 0,133" fill="#5a0a0a"/>
    </svg>
    <p class="assoc-name">Corvane Transit Assoc</p>
    <div class="total-share">
      <span>Freight Railroads=</span>
      <span class="big">1%</span>
      <span class="tail">of total transportation<br>budget</span>
    </div>
  </footer>
</main>
</body>
</html>
```